Concession stand banners for a mexican food tent

I'm looking for a clean easy to read design for a set of banners I need. More info is on the pic I uploaded. Simple modern design with just text.must say taco,burrito,burrito bowl,salad and nachos. I looking for a dark color(black or brown with colored text. I attached a picture what the setup will look like and where the banners are located.

Target Market(s)

food industry ,food truck, food tent

Font styles to use
Sans Serif

Requirements
Must have
• Must say tacos, burritos, burrito bowls, salads,nachos
Nice to have
• Easy to read from a distance.
Should not have
• hard to read text

```html
<!DOCTYPE html>
<html lang="en">
<head>
<meta charset="utf-8">
<title>Menu Banner – Mexican Food Tent</title>
<link rel="stylesheet" href="https://fonts.googleapis.com/css2?family=Alfa+Slab+One&display=swap">
<style>
  :root {
    --bg: #1e1d1a;
    --yellow: #ffea00;
    --orange: #ee7f1b;
    --green: #6aa000;
    --band: #e9a21a;
  }
  html, body {
    margin: 0;
    padding: 0;
    width: 1200px;
    height: 592px;
    overflow: hidden;
    background: var(--bg);
  }
  .banner {
    display: block;
    width: 1200px;
    height: 592px;
  }
  .banner__bg { fill: var(--bg); }
  .divider-band { stroke: var(--band); stroke-width: 22; }
  .menu-item {
    font-family: "Alfa Slab One", "Arial Black", "Helvetica Neue", Arial, sans-serif;
    font-weight: 900;
    text-anchor: middle;
    dominant-baseline: central;
    stroke-width: 3;
    stroke-linejoin: round;
    paint-order: stroke fill;
  }
  .menu-item--yellow { fill: var(--yellow); stroke: var(--yellow); }
  .menu-item--orange { fill: var(--orange); stroke: var(--orange); }
  .menu-item--green { fill: var(--green); stroke: var(--green); }
  .corner-ornament--green { fill: var(--green); }
  .corner-ornament--orange { fill: var(--orange); }
</style>
</head>
<body>
<svg class="banner" viewBox="0 0 1499 740" xmlns="http://www.w3.org/2000/svg">
  <rect class="banner__bg" width="1499" height="740"/>

  <g class="divider-bands" role="img" aria-label="Woven zigzag pattern bands in orange, yellow and green">
    <line class="divider-band" x1="-340" y1="740" x2="295" y2="0"/>
    <line class="divider-band" x1="-15" y1="740" x2="620" y2="0"/>
    <line class="divider-band" x1="310" y1="740" x2="945" y2="0"/>
    <line class="divider-band" x1="635" y1="740" x2="1270" y2="0"/>
    <line class="divider-band" x1="960" y1="740" x2="1595" y2="0"/>
  </g>

  <g class="menu">
    <text class="menu-item menu-item--yellow" font-size="150" textLength="560" lengthAdjust="spacingAndGlyphs"
          transform="translate(232 262) rotate(-49)">TACOS</text>
    <text class="menu-item menu-item--orange" font-size="150" textLength="810" lengthAdjust="spacingAndGlyphs"
          transform="translate(470 348) rotate(-49)">BURRITOS</text>
    <text class="menu-item menu-item--yellow" font-size="100" textLength="850" lengthAdjust="spacingAndGlyphs"
          transform="translate(790 372) rotate(-49)">BURRITO BOWLS</text>
    <text class="menu-item menu-item--orange" font-size="145" textLength="730" lengthAdjust="spacingAndGlyphs"
          transform="translate(1092 375) rotate(-49)">NACHOES</text>
    <text class="menu-item menu-item--green" font-size="135" textLength="540" lengthAdjust="spacingAndGlyphs"
          transform="translate(1295 492) rotate(-49)">SALADS</text>
  </g>

  <rect class="corner-ornament corner-ornament--green" x="32" y="48" width="78" height="88" rx="4"
        role="img" aria-label="Small geometric tribal diamond ornament"/>
  <rect class="corner-ornament corner-ornament--orange" x="1360" y="598" width="78" height="90" rx="4"
        role="img" aria-label="Small geometric tribal diamond ornament"/>
</svg>
</body>
</html>
```